Copperfield Wire - Subscription Landing page

we need responsive landing page for a new news service about the Blockchain innovations coins and startups, the landing page includes vertical video player and call to action button, attach mockup.
temporary page
http://www.cpfw.io/
1 page

```html
<!DOCTYPE html>
<html lang="en">
<head>
<meta charset="utf-8">
<title>Copperfield Wire – Be Ready for Tomorrow</title>
<link href="https://fonts.googleapis.com/css2?family=Montserrat:wght@500;600;700&display=swap" rel="stylesheet">
<style>
  :root {
    --red: #e0141e;
    --red-dark: #c50f18;
    --ink: #2b2b2b;
    --muted: #6a6a6a;
    --grey-mark: #5f5f5f;
    --page: #f6f6f8;
    --navy: #0b2e45;
    --pink-wash: #f8e6e8;
  }
  * { box-sizing: border-box; margin: 0; padding: 0; }
  html, body { width: 1200px; height: 677px; overflow: hidden; background: var(--page); }
  body { font-family: "Montserrat", sans-serif; color: var(--ink); }
  .canvas { position: relative; width: 1200px; height: 677px; overflow: hidden; background: var(--page); }
  .backdrop { position: absolute; inset: 0; }

  .laptop { position: absolute; left: 152px; top: 148px; width: 483px; height: 315px;
    background: #ececec; border-radius: 12px 12px 0 0; box-shadow: 0 6px 18px rgba(0,0,0,.15); }
  .laptop__screen { position: absolute; left: 23px; top: 22px; width: 439px; height: 274px;
    background: linear-gradient(180deg, #8e8584 0%, #e8b7b5 35%, #d99a95 60%, #3b3a44 100%); }
  .laptop__base { position: absolute; left: 106px; top: 460px; width: 574px; height: 10px;
    background: linear-gradient(180deg, #f0f0f0, #bdbdbd); border-radius: 0 0 40px 40px; }
  .play-btn { position: absolute; left: 360px; top: 270px; }

  .brand { position: absolute; left: 742px; top: 36px; display: flex; align-items: center; gap: 10px; }
  .brand__dot { width: 46px; height: 46px; border-radius: 50%; background: var(--red); }
  .brand__name { font-weight: 700; font-size: 27px; color: var(--red); line-height: 1; }

  .headline { position: absolute; left: 742px; top: 147px; font-size: 42px; font-weight: 700;
    line-height: 44px; color: var(--ink); }
  .lede { position: absolute; left: 742px; top: 253px; width: 300px; font-size: 17px; font-weight: 500;
    line-height: 24px; color: var(--muted); }
  .cta-label { position: absolute; left: 743px; top: 355px; width: 290px; font-size: 18px; font-weight: 600;
    line-height: 26px; color: var(--ink); }

  .cta { position: absolute; left: 743px; top: 422px; width: 212px; height: 55px;
    border: 1px solid var(--red); border-radius: 28px; }
  .cta__button { position: absolute; left: 22px; top: 4px; width: 205px; height: 45px;
    border-radius: 23px; background: linear-gradient(90deg, var(--red-dark), var(--red));
    color: #fff; font-size: 13px; font-weight: 700; letter-spacing: .3px;
    display: flex; align-items: center; justify-content: center; box-shadow: 0 4px 10px rgba(224,20,30,.3); }

  .channels { position: absolute; left: 744px; top: 511px; display: flex; gap: 7px; list-style: none; }
  .channels li { width: 41px; height: 41px; border-radius: 50%; border: 1.5px solid #333; }
</style>
</head>
<body>
<main class="canvas">
  <svg class="backdrop" width="1200" height="677" viewBox="0 0 1200 677" aria-hidden="false">
    <defs>
      <linearGradient id="wash" x1="0" y1="0" x2="1" y2="1">
        <stop offset="0" stop-color="#f7f7f9"/>
        <stop offset="1" stop-color="#f9e3e5"/>
      </linearGradient>
      <radialGradient id="network" cx=".25" cy=".55" r=".8">
        <stop offset="0" stop-color="#c65a3a"/>
        <stop offset=".45" stop-color="#3a3f52"/>
        <stop offset="1" stop-color="#0b2e45"/>
      </radialGradient>
    </defs>
    <path class="pink-wash" d="M960 0 H1200 V430 L880 590 Q770 630 760 520 V220 Q770 80 960 0 Z" fill="url(#wash)"/>
    <path class="network-field" role="img" aria-label="Glowing network of connected nodes over binary code"
          d="M0 0 H435 L660 150 Q715 195 700 260 Q690 310 640 335 L130 625 Q60 655 0 610 Z" fill="url(#network)"/>
    <g class="play-marks" fill="#666">
      <path d="M535 16 L559 29 L535 42 Z"/>
      <path d="M1089 59 L1107 69 L1089 79 Z"/>
      <path d="M1118 507 L1142 425 L1118 451 Z" opacity="0"/>
      <path d="M1118 400 L1165 426 L1118 452 Z"/>
    </g>
    <g class="play-marks play-marks--red" fill="var(--red)">
      <path d="M1115 164 L1125 169 L1115 174 Z"/>
      <path d="M1179 213 L1184 216 L1179 219 Z"/>
      <path d="M1063 355 L1068 358 L1063 361 Z"/>
      <path d="M227 532 L274 558 L227 584 Z"/>
    </g>
    <g class="play-outlines" fill="none" stroke="var(--red)" stroke-width="2">
      <path d="M559 56 L614 86 L559 116 Z"/>
      <path d="M1098 412 L1172 452 L1098 494 Z"/>
    </g>
  </svg>

  <div class="laptop">
    <div class="laptop__screen" role="img" aria-label="Video presenter standing in front of a city skyline at dusk"></div>
  </div>
  <div class="laptop__base"></div>
  <svg class="play-btn" width="70" height="76" viewBox="0 0 70 76" aria-label="Play video">
    <path d="M6 8 Q6 0 14 4 L62 32 Q68 38 62 44 L14 72 Q6 76 6 68 Z" fill="#fff"/>
  </svg>

  <header class="brand">
    <span class="brand__dot"></span>
    <span class="brand__name">Copperfield Wire</span>
  </header>

  <h1 class="headline">Be Ready for<br>Tomorrow</h1>
  <p class="lede">Stay updated with all the latest blockchain innovations coins and startups in a daily video story.</p>
  <p class="cta-label">Subscribe for free in one of your channels below:</p>

  <div class="cta">
    <a class="cta__button">BROWSE NOTIFICATION</a>
  </div>

  <ul class="channels">
    <li aria-label="Social channel 1"></li>
    <li aria-label="Social channel 2"></li>
    <li aria-label="Social channel 3"></li>
    <li aria-label="Social channel 4"></li>
    <li aria-label="Social channel 5"></li>
  </ul>
</main>
</body>
</html>
```